Open Window; Sunrise Table, River Walk Rack Card

We want an additional 2 page (front and page) 3.67" x 8.5" rack card. This rack card is now the 2nd of the series . The first one is already completed/finalized and attached (Sunrise Table River Walk Rack Card PDF).
Use the text on the word document for the included Open Window Rack card. Please use the Sunrise Table River Walk Rack card as the template to mimic. We would like all subsequent rack cards to have a similar look and feel.
The document is for older readers. Do not put text over graphics and keep it simple and easy to read with high contrast.
We want some very simple design element(s) incorporated that convey Native American communities or heritage. But NO headdress, teepee graphics, etc. At the top, of the first page we would like a collage of healthy food images. This can include fish, chicken, fresh vegetables, berries, brown rice, etc. Please remember to include the funding statement - it can be in a very small font 6/7 point. For more information about our project, please visit https://pelmorvo.org/kite-lane/

```html
<!DOCTYPE html>
<html lang="en">
<head>
<meta charset="utf-8">
<title>Sunrise Table River Walk – Open Window Rack Card</title>
<link rel="stylesheet" href="https://fonts.googleapis.com/css2?family=Open+Sans:ital,wght@0,400;0,600;0,700;0,800;1,400;1,600&family=Amatic+SC:wght@700&family=Kaushan+Script&display=swap">
<style>
  :root {
    --stage: #a6a6a6;
    --paper: #ffffff;
    --paper-grain: #f1f1f0;
    --maroon: #5a1816;
    --teal: #4aa8b4;
    --coral: #c4574c;
    --ink: #2f2f2f;
    --band-zigzag: #d8b7b0;
    --photo-warm: #9a6a45;
    --photo-green: #7c9a55;
  }
  * { box-sizing: border-box; margin: 0; padding: 0; }
  html, body { width: 1200px; height: 1097px; overflow: hidden; }
  body {
    background: var(--stage);
    font-family: "Open Sans", Arial, sans-serif;
    color: var(--ink);
    position: relative;
  }
  .rack-card {
    position: absolute;
    top: 22px;
    width: 460px;
    height: 1060px;
    background: linear-gradient(90deg, var(--paper) 0%, var(--paper-grain) 30%, var(--paper) 55%, var(--paper-grain) 80%, var(--paper) 100%);
    display: flex;
    flex-direction: column;
    overflow: hidden;
  }
  .rack-card--front { left: 33px; border: 1px solid #222; }
  .rack-card--back { left: 706px; }

  .food-collage {
    height: 162px;
    flex: none;
    background: linear-gradient(90deg, var(--photo-warm) 0%, #c9b9a3 30%, #4a3530 48%, #e8e4dc 62%, var(--photo-green) 82%, #d8c7a6 100%);
  }

  .title { text-align: center; line-height: 1.02; margin-top: 10px; }
  .title__line { display: block; font-weight: 700; font-size: 37px; letter-spacing: 0.3px; }
  .title__line--maroon { color: var(--maroon); }
  .title__line--teal { color: var(--teal); }
  .title__line--hand {
    font-family: "Amatic SC", "Comic Sans MS", cursive;
    color: var(--maroon);
    font-size: 52px;
    letter-spacing: 1px;
    line-height: 0.95;
  }

  .intro {
    font-size: 16.5px;
    line-height: 19.5px;
    text-align: justify;
    padding: 4px 18px 0 18px;
  }
  .checklist-heading {
    font-weight: 700;
    color: var(--teal);
    font-size: 16.5px;
    padding: 9px 18px 2px 18px;
  }
  .checklist-heading strong { color: var(--maroon); }
  .checklist { list-style: none; padding: 0 16px 0 20px; }
  .checklist li {
    display: flex;
    gap: 4px;
    font-size: 15.5px;
    line-height: 21px;
    text-align: justify;
  }
  .tick { flex: none; width: 15px; height: 15px; margin-top: 3px; }
  .doctor-note {
    color: var(--coral);
    font-weight: 700;
    font-size: 15.5px;
    line-height: 19px;
    text-align: center;
    padding: 10px 18px 0 18px;
  }

  .zigzag-band {
    height: 16px;
    flex: none;
    background: linear-gradient(180deg, #f3e7e4, var(--band-zigzag), #f3e7e4);
  }
  .heritage-band {
    background: var(--maroon);
    color: #fff;
    font-size: 12.5px;
    line-height: 17px;
    text-align: center;
    padding: 6px 12px;
  }
  .footer-bottom { margin-top: auto; display: flex; flex-direction: column; }

  .pull-quote {
    position: relative;
    font-style: italic;
    font-size: 13.5px;
    line-height: 17px;
    padding: 12px 42px 10px 40px;
  }
  .pull-quote__mark {
    position: absolute;
    color: var(--teal);
    font-weight: 800;
    font-style: normal;
    font-size: 30px;
    line-height: 1;
  }
  .pull-quote__mark--open { left: 14px; top: 10px; }
  .pull-quote__mark--close { right: 16px; bottom: 0; }

  .site-bar {
    background: var(--teal);
    color: #fff;
    text-align: center;
    font-weight: 700;
    font-style: italic;
    font-size: 19px;
    height: 35px;
    line-height: 35px;
    flex: none;
  }

  /* back */
  .title--recipe .title__line { font-size: 44px; line-height: 1.0; }
  .recipe-name {
    font-family: "Kaushan Script", cursive;
    color: var(--teal);
    font-size: 17px;
    padding: 14px 0 6px 16px;
  }
  .recipe-top { display: flex; gap: 6px; padding: 0 14px 0 16px; }
  .stew-photo {
    flex: none;
    width: 202px;
    height: 156px;
    background: radial-gradient(ellipse at 50% 55%, #b88a5a 0%, #7a4f2e 45%, #c9c2b8 75%, #e6e1da 100%);
  }
  .ingredients__heading {
    font-family: "Amatic SC", cursive;
    color: var(--coral);
    font-size: 24px;
    line-height: 1;
  }
  .ingredients__list { list-style: none; }
  .ingredients__list li {
    display: flex;
    gap: 3px;
    font-style: italic;
    font-size: 10.5px;
    line-height: 13px;
    text-align: justify;
  }
  .ingredients__list .tick { width: 11px; height: 11px; margin-top: 1px; }
  .method {
    font-size: 17.5px;
    line-height: 24px;
    text-align: center;
    padding: 10px 16px 0 16px;
  }
  .yield { display: block; font-style: italic; }
  .info {
    text-align: center;
    padding: 14px 10px 0 10px;
    font-size: 12.5px;
    line-height: 17px;
  }
  .info__heading { color: var(--teal); font-weight: 700; font-size: 19px; line-height: 24px; }
  .info__topic { font-weight: 700; }
  .info__source { font-style: italic; }
  .org-mark {
    display: flex;
    align-items: center;
    justify-content: center;
    gap: 10px;
    padding: 14px 0 12px 0;
  }
  .org-mark__dot { width: 40px; height: 40px; border-radius: 50%; background: var(--teal); }
  .org-mark__name { color: var(--teal); font-weight: 700; font-size: 19px; }
</style>
</head>
<body>
<svg width="0" height="0" style="position:absolute">
  <symbol id="tick" viewBox="0 0 16 16">
    <rect x="1" y="3" width="12" height="12" fill="#fff" stroke="#4aa8b4" stroke-width="2"/>
    <path d="M3.5 8.5 L7 12 L15 2" fill="none" stroke="#c4574c" stroke-width="2.4" stroke-linecap="round" stroke-linejoin="round"/>
  </symbol>
</svg>

<article class="rack-card rack-card--front">
  <div class="food-collage" role="img" aria-label="Collage of healthy foods: grilled chicken, wild rice, olive oil, eggs, nuts and fresh salad"></div>
  <h1 class="title">
    <span class="title__line title__line--maroon">SUNRISE TABLE</span>
    <span class="title__line title__line--teal">RIVER WALK</span>
    <span class="title__line title__line--hand">OPEN WINDOW</span>
  </h1>
  <p class="intro">Making small changes in what and how you eat can make you feel better and stay healthier longer. Healthy food choices may be good for your brain, energy, mood, and health.</p>
  <p class="checklist-heading">Little changes that make a <strong>big difference:</strong></p>
  <ul class="checklist">
    <li><svg class="tick"><use href="#tick"/></svg><span>Start today!</span></li>
    <li><svg class="tick"><use href="#tick"/></svg><span>Write down what, when, and how much you eat for three days</span></li>
    <li><svg class="tick"><use href="#tick"/></svg><span>Set SMART goals (Specific, Measurable, Attainable, Relevant &amp; Timebound), like: “I will eat one piece of fruit at breakfast three times this week.”</span></li>
    <li><svg class="tick"><use href="#tick"/></svg><span>Make just 1 or 2 changes at a time until they become a habit</span></li>
    <li><svg class="tick"><use href="#tick"/></svg><span>Focus more on eating healthy food versus not eating unhealthy food</span></li>
    <li><svg class="tick"><use href="#tick"/></svg><span>Make a game plan for the times you get tempted to eat unhealthy foods</span></li>
    <li><svg class="tick"><use href="#tick"/></svg><span>Involve the whole family in setting goals</span></li>
    <li><svg class="tick"><use href="#tick"/></svg><span>Name your main reason to eat healthier and feel better, like “More energy to go to church and tribal cultural events.”</span></li>
  </ul>
  <p class="doctor-note">Talk to your doctor about healthier eating to make you feel better and stay healthier longer.</p>
  <div class="footer-bottom">
    <div class="zigzag-band" role="img" aria-label="Zigzag heritage pattern band"></div>
    <p class="heritage-band">“When it comes to traditional foods, for me it’s something more than just food, it’s my heritage.” Delra Sonn (Saguaro Flats Community)</p>
    <div class="zigzag-band" role="img" aria-label="Zigzag heritage pattern band"></div>
    <p class="pull-quote"><span class="pull-quote__mark pull-quote__mark--open">“</span>Making small, practical changes can help you achieve your health goals.<span class="pull-quote__mark pull-quote__mark--close">”</span></p>
    <div class="site-bar">www.pelmorvo.org</div>
  </div>
</article>

<article class="rack-card rack-card--back">
  <div class="food-collage" role="img" aria-label="Collage of healthy foods: grilled chicken, wild rice, olive oil, eggs, nuts and fresh salad"></div>
  <h2 class="title title--recipe">
    <span class="title__line title__line--maroon">MAKE THIS</span>
    <span class="title__line title__line--maroon">AT HOME</span>
  </h2>
  <p class="recipe-name">O’odham White Tepary Bean Stew</p>
  <div class="recipe-top">
    <div class="stew-photo" role="img" aria-label="Wooden bowl of white bean stew with meat"></div>
    <div class="ingredients">
      <p class="ingredients__heading">INGREDIENTS:</p>
      <ul class="ingredients__list">
        <li><svg class="tick"><use href="#tick"/></svg><span>1 cup dried tepary beans, rinsed &amp; picked through (substitute Navy Beans or Great Northern beans)</span></li>
        <li><svg class="tick"><use href="#tick"/></svg><span>10 cups of water</span></li>
        <li><svg class="tick"><use href="#tick"/></svg><span>1 tsp. salt</span></li>
        <li><svg class="tick"><use href="#tick"/></svg><span>1 lb. oxtails, beef short ribs, deer, rabbit, or chicken</span></li>
      </ul>
    </div>
  </div>
  <p class="method">Put beans, water, and salt in a stockpot. Bring to a boil, reduce heat and simmer, covered, for one hour and a half. Add meat to the bean mixture, cover and cook for one more hour, or until beans are tender and meat is falling off the bone. If using a crockpot, place water and all other ingredients in the pot, cover, and set to high. Cook for 8 hours or until the meat is falling off the bone and the beans are tender. <span class="yield">Makes 8 – 10 cups.</span></p>
  <div class="footer-bottom">
    <div class="zigzag-band" role="img" aria-label="Zigzag heritage pattern band"></div>
    <p class="heritage-band">Elders are our keepers of traditional knowledge about food and ways of life. You play an important role in sharing this knowledge with younger generations.</p>
    <div class="zigzag-band" role="img" aria-label="Zigzag heritage pattern band"></div>
    <div class="info">
      <p class="info__heading">FOR MORE INFORMATION</p>
      <p class="info__topic">About Goal Setting</p>
      <p class="info__source">Council for Plate Wellness</p>
      <p>https://pelmorvo.org/goal-video</p>
      <p class="info__source">Brightmoor Health Institute</p>
      <p>https://pelmorvo.org/smart-goals</p>
    </div>
    <div class="org-mark">
      <span class="org-mark__dot"></span>
      <span class="org-mark__name">KITE LANE RESOURCE CENTER</span>
    </div>
    <div class="site-bar">www.pelmorvo.org</div>
  </div>
</article>
</body>
</html>
```